Design and put together a 5 page A4 brochure for a Training Programme

Carrowmere Institute of Training deliver a Nationally Accredited Programme in Medical Reception and Administration.

We have a new Qualification (Cert III Business Administration) and we require a 5 page brochure to be designed. (I have CHANGED THIS TO 5 Pages as I can see it is too crowded and not clean enough)

I would put a 6th page in as an application form.

We have recently rebranded our website which is currently under development - so a .jpg will be available of the 'look and feel of this'. I will also upload some stock photos which could be used in the design.

This is an important project for us - so your fantastic work will be greatly appreciated.

This project is fairly urgent - so it is likely we will be choosing a 'winner' to work with sooner rather than later.

Thanks for considering!

I will be uploading various graphics/drafts now.
Updates

Target Market(s)

1/ Women 25-45 yrs undertaking studies in being a medical receptionist
2/ Medical Practices who are hiring Trainees for their medical clinic or hospital

Industry/Entity Type

Medical

Font styles to use
Serif
Sans Serif

Colors
0455a3
fbe7d2
f68e4e
fef4ee
3176b5
33a6d7
f37122

Requirements
Must have
• Clear and clean design - professional
• Graphics of medical pictures (I will supply some so you get the look and feel of wht we are looking for)
• Corporate branding (I will upload a .jpg of new website design for look and feel
• The colour I would like with blue is also a STONE colour - I could not find it in the colour wheel on this site.
• The partner logos should be on the last page probably in one faded colour (such as grey)
Should not have
• I must be able to see the inside of the brochure also, I can not pick this purely on the front cover. Thanks :-)
• I have also now updated the Company Logo

```html
<!DOCTYPE html>
<html lang="en">
<head>
<meta charset="utf-8">
<title>Student Study Package – Cert III Business Admin (Medical)</title>
<link href="https://fonts.googleapis.com/css2?family=Arimo:wght@400;700&display=swap" rel="stylesheet">
<style>
  :root{
    --navy:#0455a3;
    --blue:#3176b5;
    --sky:#33a6d7;
    --orange:#f37122;
    --orange-soft:#f68e4e;
    --peach:#fbe7d2;
    --cream:#fef4ee;
    --grey:#5a5a5a;
    --white:#ffffff;
  }
  *{box-sizing:border-box;margin:0;padding:0}
  html,body{width:848px;height:1200px;overflow:hidden;background:var(--white)}
  body{font-family:"Arimo",Arial,sans-serif;color:var(--grey);font-size:12px;line-height:15.6px}
  .page{position:relative;width:848px;height:1200px;overflow:hidden}
  .backdrop{position:absolute;inset:0}
  .block{position:absolute}
  h2{color:var(--navy);font-weight:400;font-size:19.5px;line-height:23px;letter-spacing:-.1px}
  .lead{color:var(--navy);margin-top:3px}
  .blue{color:var(--navy)}
  b{font-weight:700}

  .package{left:40px;top:50px;width:640px}
  .lists{left:40px;top:98px;width:730px;display:flex}
  .lists ul{list-style:none}
  .lists ul:first-child{width:388px}
  .lists ul:last-child{width:340px}
  .lists li{position:relative;padding-left:20px}
  .lists li::before{content:"•";position:absolute;left:2px;font-size:10px;color:#888}
  .lists li.beside-bag{max-width:240px}

  .bag{position:absolute;left:690px;top:54px;width:104px;height:120px}

  .main-col{left:40px;top:360px;width:540px}
  .main-col h2{margin-bottom:4px}
  .main-col p{margin-bottom:12px}
  .main-col h2.second{margin-top:16px}

  .portrait{position:absolute;left:598px;top:276px;width:250px;height:568px}
  .desk-photo{position:absolute;left:40px;top:904px;width:238px;height:256px}

  .assessment{left:299px;top:905px;width:510px}
  .assessment p{color:var(--navy);margin-bottom:8px}
  .assessment .duration{color:var(--orange);font-size:14px;margin:2px 0 10px}
  .assessment h2.support{margin-top:12px;margin-bottom:4px}
</style>
</head>
<body>
<div class="page">

  <svg class="backdrop" width="848" height="1200" viewBox="0 0 848 1200" aria-hidden="true">
    <defs>
      <linearGradient id="peachFill" x1="0" y1="0" x2="0" y2="1">
        <stop offset="0" stop-color="#fbe7d2"/>
        <stop offset=".4" stop-color="#fef4ee"/>
        <stop offset="1" stop-color="#fef4ee"/>
      </linearGradient>
      <linearGradient id="topStripe" x1="0" y1="0" x2="1" y2="0">
        <stop offset="0" stop-color="#f37122"/>
        <stop offset=".55" stop-color="#f68e4e"/>
        <stop offset="1" stop-color="#fbe7d2" stop-opacity=".4"/>
      </linearGradient>
      <linearGradient id="lowStripe" x1="0" y1="0" x2="1" y2="0">
        <stop offset="0" stop-color="#fbe7d2" stop-opacity="0"/>
        <stop offset=".35" stop-color="#f68e4e"/>
        <stop offset="1" stop-color="#f37122"/>
      </linearGradient>
    </defs>
    <polygon points="0,348 848,290 848,838 0,895" fill="url(#peachFill)"/>
    <polygon points="0,336 848,276 848,288 0,350" fill="url(#topStripe)"/>
    <polygon points="220,893 848,826 848,858 380,892" fill="url(#lowStripe)"/>
  </svg>

  <div class="bag" role="img" aria-label="Red tote bag holding the student study package" style="background:linear-gradient(160deg,#e8302a,#c41d1d);border-radius:4px 4px 8px 8px"></div>

  <section class="block package">
    <h2>THE STUDENT STUDY PACKAGE – WHAT YOU RECEIVE</h2>
    <p class="lead">Students receive an array of helpful resources to keep as part of the Carrowmere Programme. These include :</p>
  </section>

  <div class="block lists">
    <ul>
      <li>Carrowmere Institute Workbook ‘Medical Receptionist and Secretary’s Handbook’</li>
      <li>Carrowmere Institute Workbook ‘Write, Design and Produce Documents for the Australian Medical Office’</li>
      <li>Carrowmere Institute Workbook ‘Medical Triage and Customer Service for non-clinical staff’</li>
      <li>Access to Carrowmere Online Learning platform</li>
      <li>Access to Carrowmere Type-fast programme with testing and certification to Australian standards</li>
      <li>Scrivo Word and Layout online tutorials and certification</li>
      <li>Digital Medical Transcription Software – student version.</li>
    </ul>
    <ul>
      <li class="beside-bag">Medical Accounts Software Clinidesk – demo version to keep</li>
      <li class="beside-bag">9CPMG endorsed Triage Guide Chart</li>
      <li class="beside-bag">Civic Aid Society Basic First Aid Booklet and CPR Wallet Card</li>
      <li>CPR Accredited Training</li>
      <li>Cardiac Care Council endorsed online training programme</li>
      <li>Cardiac Care Council DVD and Facts Pack for medical professionals</li>
      <li>Access to accredited specialist mentors and trainers</li>
      <li>Registration into Carrowmere’s Job-Network Club</li>
    </ul>
  </div>

  <div class="portrait" role="img" aria-label="Smiling medical professional in a white coat with a stethoscope"
       style="background:linear-gradient(180deg,#e9eef4 0%,#f4f6f9 40%,#dfe6ee 100%);clip-path:polygon(0 3%,100% 0,100% 97.5%,0 100%)"></div>

  <section class="block main-col">
    <h2>ENTRY REQUIREMENTS</h2>
    <p>There are no formal entry requirements for this qualification, however it is recommended that individuals have a Year 10 standard of English and basic keyboard skills. Students with English as a second language may request a language, literacy and numeracy assessment during the enrolment and orientation session to determine learning support needs.</p>

    <h2 class="second">UNIQUE DELIVERY MODEL – COMBINING FACE-TO-FACE LEARNING WITH SELF PACED</h2>
    <p>The Carrowmere Cert III Business Admin (Medical) Programme offers a <b>unique structure</b> to the medical administrative trainee - offering flexibility, <b>intensive face-to-face training of crucial medical units combined with a self-paced home learning and a unique online learning programme.</b> This allows studies to be undertaken at a convenient time by students and trainees.</p>
    <p>The programme will adjust to differing skill levels and ability to commit time to the programme and can be completed in as little as 6 months to a maximum of 12 months – depending on prior experience and skills.</p>
    <p class="blue">Carrowmere believe some units can only be taught effectively with face to face training led by industry experts and cannot be taught effectively by online learning alone. Therefore Carrowmere’s Core Medical units are taught in workshop settings in 5 Saturdays (or through the week by prior arrangement) followed by self-paced and online delivery of core administration modules. The programme is further followed up with an intensive one day workshop.</p>
    <p class="blue">For Traineeships, our Trainers physically attend site 1-2 times for personalised mentoring. There is a mentor/trainer assessor available at all times during our programme for all students.</p>
    <p class="blue">All students are invited to Carrowmere’s Computing Medical Software workshop day, where students work hands-on in a workplace simulated environment. Participants receive a complimentary demo copy of a Popular Medical software programme.</p>
  </section>

  <div class="desk-photo" role="img" aria-label="Smiling student working at a laptop"
       style="background:linear-gradient(135deg,#eef2f6 0%,#d7e2ee 55%,#c9d6e4 100%)"></div>

  <section class="block assessment">
    <h2>COMBINED ASSESSMENT APPROACH</h2>
    <p class="duration">Duration:&nbsp;&nbsp; 6 –12 months</p>
    <p>Carrowmere utilise a variety of assessment processes which allow different learning styles to benefit from our programme. Assessment tools may include questioning, quizzes, assignments, projects, case studies and more.</p>
    <p>Workplace project work simulates real workplace activities utilising real medical forms, situations, case histories, resources, practice software and represents industry standards including CPMG, MPA, the National Clinical Board, Civic Aid Society and the Cardiac Care Council.</p>
    <h2 class="support">STUDENT SUPPORT</h2>
    <p>Students have direct access to a Trainer/Mentor for the duration of the programme and have direct access to Carrowmere Health Student On-Line Forum which students can engage with fellow students and trainers from across Australia.</p>
  </section>

</div>
</body>
</html>
```